Mental Health Therapy Website

I need a design for a mental health therapy website. It is a private practice. The business name is Brindle Counseling, PLLC. My name is Martin Hale, LMHC, NCC, DCC. I would like some of the features/menus to be Home; Welcome/About Me, Rates and Services, Common Questions, and Contact.
If possible I would like a blog on the main page that I can update with articles I write. I would like the contact page to feature a map to my location (4318 Cedarbend Ave. E, Lakewood, WA 98499).
I would like to place a small photo of me on the Welcome/About page.
I am new to this so if I am forgetting anything, please ask me!!
I will upload my logo so you can fit it and the color scheme into the design.
Thank you so very much!

```html
<!DOCTYPE html>
<html lang="en">
<head>
<meta charset="utf-8">
<title>Brindle Counseling</title>
<link href="https://fonts.googleapis.com/css2?family=Cinzel:wght@700&family=Open+Sans:wght@400;600&display=swap" rel="stylesheet">
<style>
:root{
  --blue:#2a63a6;
  --blue-dark:#1f4f8c;
  --blue-light:#4a8ac8;
  --green:#6f9a2e;
  --green-light:#8ab83a;
  --green-dark:#4f7d2c;
  --text:#6a6a6a;
  --line:#d9d9d9;
  --page:#ffffff;
}
*{margin:0;padding:0;box-sizing:border-box}
html,body{width:1200px;height:1143px;overflow:hidden;background:var(--page)}
body{position:relative;font-family:"Open Sans",sans-serif;color:var(--text)}
.backdrop{position:absolute;left:0;top:6px;width:1200px;height:400px;background:linear-gradient(#ffffff 0%,#fbfbfd 40%,#e9e8f0 100%)}
.topline{position:absolute;left:0;top:0;width:1200px;height:6px;background:#ececec}
.brand{position:absolute;left:90px;top:30px;display:flex;align-items:center;gap:14px}
.brand-dot{width:76px;height:76px;border-radius:50%;background:var(--blue)}
.brand-name{font-family:"Open Sans",sans-serif;font-weight:600;font-size:30px;line-height:34px;color:var(--blue);width:200px}
.appointment{position:absolute;right:96px;top:55px;text-align:right}
.appointment-label{font-size:16px;color:var(--blue)}
.appointment-phone{font-size:27px;color:var(--green);line-height:34px}
.main-nav{position:absolute;left:90px;top:125px;width:1026px;height:52px;border-radius:4px 4px 0 0;background:linear-gradient(#4a8ccb,#2c69ac 55%,#235a99);display:flex}
.main-nav a{display:block;height:52px;line-height:52px;padding:0 25px;color:#fff;text-decoration:none;font-size:16px;text-transform:uppercase;border-right:1px solid rgba(255,255,255,.25);box-shadow:1px 0 0 rgba(0,0,0,.12)}
.main-nav a:first-child{padding:0 26px 0 44px}
.hero{position:absolute;left:90px;top:177px;width:1026px;height:367px;border:1px solid #ddd;border-top:none;border-radius:0 0 5px 5px;background:#fff;box-shadow:0 6px 10px rgba(0,0,0,.05)}
.hero-photo{position:absolute;left:0;top:0;width:1016px;height:366px;background:linear-gradient(100deg,#d9c9a3 0%,#efe4c8 35%,#c9a27a 55%,#8ec8d8 75%,#f1ece0 100%)}
.hero-title{position:absolute;left:198px;top:124px;font-family:"Cinzel",serif;font-weight:700;color:var(--blue-dark);text-shadow:0 0 2px #fff,0 0 2px #fff,0 0 3px #fff}
.hero-title .main{font-size:44px;line-height:50px;display:block}
.hero-title .sub{font-size:24px;line-height:30px;display:block}
.hero-dots{position:absolute;left:485px;top:345px;display:flex;gap:4px}
.hero-dots span{width:11px;height:11px;border-radius:50%;background:#fff;opacity:.9}
.welcome{position:absolute;left:94px;top:586px;width:712px}
.section-title{font-family:"Cinzel",serif;font-weight:700;font-size:27px;color:var(--blue);line-height:36px}
.section-title .accent{color:var(--green)}
.body-copy{font-size:13px;line-height:24px;color:var(--text)}
.welcome .body-copy{margin-top:6px;padding-left:3px}
.divider{position:absolute;left:97px;top:778px;width:712px;height:1px;background:var(--line)}
.about{position:absolute;left:101px;top:795px;width:690px}
.about-photo{position:absolute;left:-2px;top:44px;width:139px;height:131px;background:linear-gradient(160deg,#e4e4e0,#b89680 50%,#5d5b4a)}
.about .body-copy{position:absolute;left:152px;top:37px;width:535px}
.services{position:absolute;left:839px;top:585px;width:271px;height:327px;border-radius:3px;background:linear-gradient(#8ab83a,#6c9e33 55%,#4f7d2c);padding:18px 29px 0 33px}
.services-title{color:#fff;font-size:22px;line-height:32px;margin-bottom:4px}
.services ul{list-style:none}
.services li{font-size:13px;color:#f1f7e6;height:28px;line-height:27px;border-bottom:1px solid rgba(255,255,255,.2);padding-left:14px;position:relative}
.services li:last-child{border-bottom:none}
.services li::before{content:"";position:absolute;left:1px;top:10px;border-left:5px solid #fff;border-top:4px solid transparent;border-bottom:4px solid transparent}
.site-footer{position:absolute;left:0;top:1033px;width:1200px;height:110px;background:linear-gradient(#5d84b8,#3d6aa6 50%,#2c5a98);border-top:1px solid #8aa6cc}
.footer-nav{position:absolute;left:97px;top:26px;font-size:15px;color:#fff}
.footer-nav a{color:#fff;text-decoration:none}
.footer-nav .sep{margin:0 9px}
.copyright{position:absolute;left:97px;top:58px;font-size:11.5px;color:#e6edf6}
.social{position:absolute;left:966px;top:22px;display:flex;gap:4px}
.social span{width:28px;height:28px;border-radius:50%;background:#f4f6f9}
</style>
</head>
<body>
<div class="topline"></div>
<div class="backdrop"></div>

<header>
  <div class="brand">
    <div class="brand-dot"></div>
    <div class="brand-name">Brindle Counseling</div>
  </div>
  <div class="appointment">
    <div class="appointment-label">Make Appointment</div>
    <div class="appointment-phone">685-555-0142</div>
  </div>
</header>

<nav class="main-nav">
  <a href="#">Home</a>
  <a href="#">About Me</a>
  <a href="#">Rates and Services</a>
  <a href="#">Common Questions</a>
  <a href="#">Contact</a>
</nav>

<section class="hero">
  <div class="hero-photo" role="img" aria-label="Photo of a therapist talking with a client on a sofa beside a lamp"></div>
  <div class="hero-title">
    <span class="main">Mental Health Therapy</span>
    <span class="sub">Lorem ipsum dolor sit amet consectetuer</span>
  </div>
  <div class="hero-dots"><span></span><span></span><span></span><span></span></div>
</section>

<section class="welcome">
  <h1 class="section-title"><span class="accent">Welcome to</span> Brindle Counselling homepage</h1>
  <p class="body-copy">Phasellus felis dolor scelerisque a tempus eget lobortis id libero Aliquam nec erat at purus cursus interdum Vestibulum ligula augue bibendum accumsan vestibulum ut commodo a mi Morbi ornare gravida elit Integer congue augue et male-suada iaculis ipsum dui aliquet felis at cursus magna nisl nec elit Vestibulum gravida Praesent elementum elit at tellus Malesuada nec ultricies sit amet porttitor mattis enim In massa libero interdum nec interdum vel blandit sed nulla In ullamcorper est eget tempor cursus neque mi consectetuer mi a ultricies massa est sed nis</p>
</section>

<div class="divider"></div>

<section class="about">
  <h2 class="section-title">Little About Me</h2>
  <div class="about-photo" role="img" aria-label="Portrait photo of the therapist"></div>
  <p class="body-copy">Mental health counseling/therapy for individuals (children, adolescents, adults), couples, and families.&nbsp; I am a trauma certified therapist that utilizes CBT+ to assist with trauma. My approach to therapy is psychodynamic that utilizes tools from CBT, Solutions-focused, Emotions-focused, and Psychoeducation therapies to assist clients managing depression, anxiety, truama, phobias, personality disorders, ADHD, self-injury,and communication issues.&nbsp; Sessions are typically 45 to 50 minutes in length.</p>
</section>

<aside class="services">
  <h3 class="services-title">Services Provides</h3>
  <ul>
    <li>Etiam eu urna Sed</li>
    <li>Porta Suspendisse quam</li>
    <li>Leo molestie sed luctus</li>
    <li>Feugiat in pede Fusce tellus</li>
    <li>Sed metus augue convallis</li>
    <li>Et vehicula ut pulvinar</li>
    <li>Eu ante Integer</li>
    <li>Tellus tristique vitae</li>
    <li>Consequat nec porta</li>
  </ul>
</aside>

<footer class="site-footer">
  <div class="footer-nav">
    <a href="#">Home</a><span class="sep">|</span><a href="#">About Me</a><span class="sep">|</span><a href="#">Rates and Services</a><span class="sep">|</span><a href="#">Common Questions</a><span class="sep">|</span><a href="#">Contact</a>
  </div>
  <div class="copyright">© 2012 Company Name.&nbsp; All right reserved.&nbsp; Term of Use</div>
  <div class="social"><span></span><span></span><span></span><span></span></div>
</footer>
</body>
</html>
```